Pain Management, Personal Injury & Motor Vehicle Accident

I need t rack card to use as marketing collateral while talking to urgent cares, wreckers services, primary care, and emergency room staff
If you have been involved in a motor vehicle accident or personal injury accident, Prairie Ridge Pain Specialist is your Solution to complete pain relief. We understand your pain and are here to assist you along the journey to becoming pain free. It is crucial that you choose a physician who is experienced in treating your unique injury.
At Prairie Ridge Pain Specialist, Dr Calvin Hardesty and his team of experts will provide you with a specialized approach to reducing and managing your pain with a comprehensive and effective treatment plan based on a proper diagnosis. You can expect an exceptional treatment program for your injuries to help you to begin improving your quality of life immediately.
We treat:
Car Accident Injuries
Semi Truck Injuries
Most Personal Injuries
Slip and Falls
Motorcycle Accident Injuries
Whiplash
Back Injuries
Neck Injuries
Shoulder Injuries
Headaches
Locations: Cedar Bluff, Harlan, Millbrook
Phone: (580) 472-6193
Fax: (833) 748-2954
www.prairieridgepainclinic.com
Target Market(s)
Urgent Cares, Emergency Rooms, Primary Care, Wrecker Services, anyone involved in a Personal Injury or Motor Vehicle Accident
Industry/Entity Type
Healthcare, Motor Vehicle Accident Injury, Personal Injury, Pain Management, Pain Relief

```html
<!DOCTYPE html>
<html lang="en">
<head>
<meta charset="utf-8">
<title>Prairie Ridge Pain Specialists – Rack Card</title>
<link rel="stylesheet" href="https://fonts.googleapis.com/css2?family=Merriweather:wght@400;700&family=Open+Sans:wght@400;600;700&display=swap">
<style>
:root{
  --red:#d0141a;
  --red-deep:#8e0c10;
  --black:#161616;
  --white:#ffffff;
  --grey-bg:#a9a9a9;
  --list-text:#ffe1d6;
  --body-text:#3a3a3a;
}
*{box-sizing:border-box;margin:0;padding:0}
html,body{width:773px;height:1200px;overflow:hidden}
body{background:var(--grey-bg);position:relative;font-family:"Open Sans",Arial,sans-serif}
.card{position:absolute;top:215px;width:345px;height:770px;overflow:hidden;box-shadow:0 6px 14px rgba(0,0,0,.35)}
.card--front{left:27px;background:var(--white)}
.card--back{left:401px;background:var(--red)}
.card__bg{position:absolute;inset:0;width:345px;height:770px}
.abs{position:absolute}

/* front */
.brand{position:absolute;left:40px;top:72px;display:flex;align-items:center;gap:12px}
.brand__dot{width:50px;height:50px;border-radius:50%;background:var(--black)}
.brand__text{font-family:"Merriweather",Georgia,serif;color:var(--black);font-size:11px;line-height:1.45}
.brand__name{font-size:12px;border-bottom:1.5px solid var(--red);padding-bottom:2px;margin-bottom:2px}
.brand__doctor{font-size:9px}
.hero-photo{left:200px;top:205px;width:145px;height:250px;background:radial-gradient(ellipse at 55% 45%,#e8a070 0%,#8a4a30 30%,#3a2018 60%,rgba(22,22,22,0) 80%)}
.title{left:30px;top:265px;font-family:"Merriweather",Georgia,serif;font-weight:700;color:var(--white);font-size:23px;line-height:1.2}
.title__rule{left:30px;top:349px;width:170px;height:2px;background:var(--red)}
.tagline{left:32px;top:356px;font-family:"Merriweather",Georgia,serif;color:var(--white);font-size:11.5px}
.bubble{position:absolute;border-radius:50%;border:4px solid var(--red)}
.bubble--a{left:38px;top:410px;width:84px;height:84px;background:linear-gradient(150deg,#8a8f98,#4a4d52)}
.bubble--b{left:114px;top:388px;width:122px;height:122px;background:linear-gradient(150deg,#f1e6e1,#d9a79a);z-index:2}
.bubble--c{left:224px;top:410px;width:84px;height:84px;background:linear-gradient(150deg,#f4ece6,#d8c0b0)}
.intro{left:28px;top:522px;width:290px;font-size:8.1px;line-height:1.42;color:var(--body-text);text-align:center}
.intro p+p{margin-top:6px}

/* shared contact */
.phone-pill{position:absolute;left:60px;top:650px;height:30px;padding:0 12px 0 4px;border-radius:15px;background:var(--red);display:flex;align-items:center;gap:7px;color:var(--white);font-family:"Merriweather",Georgia,serif;font-size:20px;font-weight:700;white-space:nowrap;z-index:3}
.phone-pill__icon{width:23px;height:23px;border-radius:50%;background:var(--white);display:flex;align-items:center;justify-content:center}
.contact{position:absolute;left:0;top:697px;width:345px;text-align:center;color:var(--white);font-family:"Merriweather",Georgia,serif;font-size:13.5px;line-height:21px}
.contact__row{display:flex;justify-content:center;align-items:center;gap:7px}

/* back */
.treat-head{left:35px;top:18px;width:275px;height:38px;display:flex;align-items:center}
.treat-head__line{flex:1;height:3px;background:var(--black)}
.treat-head__pill{background:var(--black);color:var(--white);font-family:"Merriweather",Georgia,serif;font-weight:700;font-size:22px;padding:4px 18px;border-radius:18px}
.treat-list{position:absolute;list-style:none;color:var(--list-text);font-weight:600;font-size:15.5px;line-height:19.5px}
.treat-list li{position:absolute;left:0;width:150px;padding-left:22px;white-space:nowrap}
.treat-list li svg{position:absolute;left:0;top:3px}
.treat-list--left{left:34px;top:75px}
.treat-list--right{left:198px;top:75px}
.treat-divider{left:178px;top:78px;height:222px;border-left:2px dotted rgba(0,0,0,.55)}
.lifestyle-photo{left:0;top:340px;width:345px;height:350px;background:linear-gradient(170deg,#7a8c55 0%,#4e6638 45%,#a8a48e 75%,#6b6a5c 100%)}
.staff{position:absolute;border-radius:50%;border:4px solid #f2f2f2}
.staff--one{left:129px;top:324px;width:106px;height:106px;background:linear-gradient(#eef1ee,#4fae95);z-index:2}
.staff--two{left:213px;top:300px;width:129px;height:129px;background:linear-gradient(#f3f3f3,#d52a25);z-index:2}
</style>
</head>
<body>

<section class="card card--front" aria-label="Rack card front">
  <svg class="card__bg" viewBox="0 0 345 770" aria-hidden="true">
    <defs>
      <linearGradient id="frontLower" x1="0" y1="0" x2="0" y2="1">
        <stop offset="0" stop-color="#d9d9d9"/><stop offset="1" stop-color="#ffffff"/>
      </linearGradient>
    </defs>
    <rect width="345" height="770" fill="#fff"/>
    <path d="M0 250 C110 235 230 195 345 168 L345 190 C230 215 110 255 0 272 Z" fill="#d0141a"/>
    <path d="M0 272 C110 255 230 215 345 190 L345 420 C240 440 120 455 0 478 Z" fill="#161616"/>
    <path d="M0 478 C120 455 240 440 345 420 L345 700 L0 700 Z" fill="url(#frontLower)"/>
    <path d="M0 440 C100 420 200 430 345 400 L345 418 C220 440 110 455 0 476 Z" fill="#d0141a"/>
  </svg>

  <div class="brand">
    <span class="brand__dot"></span>
    <div class="brand__text">
      <div>Hardesty Medical, LLC dba</div>
      <div class="brand__name">Prairie Ridge Pain Specialists</div>
      <div class="brand__doctor">Dr. Calvin Hardesty, MD</div>
    </div>
  </div>

  <div class="abs hero-photo" role="img" aria-label="Photo of a hand holding a knee with the joint highlighted in glowing orange"></div>

  <h1 class="abs title">Prairie Ridge<br>Pain Specialists</h1>
  <div class="abs title__rule"></div>
  <p class="abs tagline">Relieving Pain, Improving Lives</p>

  <div class="bubble bubble--a" role="img" aria-label="Photo of a motorcycle accident scene"></div>
  <div class="bubble bubble--b" role="img" aria-label="Photo of a woman holding her sore shoulder"></div>
  <div class="bubble bubble--c" role="img" aria-label="Photo of a therapist treating a patient's foot"></div>

  <div class="abs intro">
    <p>If you have been involved in a motor vehicle accident or personal injury accident, Prairie Ridge Pain Specialist is your Solution to complete pain relief. We understand your pain and are here to assist you along the journey to becoming pain free. It is crucial that you choose a physician who is experienced in treating your unique injury.</p>
    <p>At Prairie Ridge Pain Specialist, Dr Calvin Hardesty and his team of experts will provide you with a specialized approach to reducing and managing your pain with a comprehensive and effective treatment plan based on a proper diagnosis. You can expect an exceptional treatment program for your injuries to help you to begin improving your quality of life immediately.</p>
  </div>

  <svg class="card__bg" viewBox="0 0 345 770" aria-hidden="true" style="z-index:1">
    <path d="M0 700 C120 682 240 676 345 700 L345 770 L0 770 Z" fill="#161616"/>
    <path d="M250 672 C290 676 320 684 345 698 L345 706 C318 694 290 686 250 680 Z" fill="#d0141a"/>
  </svg>

  <div class="phone-pill">
    <span class="phone-pill__icon"><svg width="13" height="13" viewBox="0 0 24 24"><path fill="#d0141a" d="M6.6 10.8a15 15 0 0 0 6.6 6.6l2.2-2.2c.3-.3.7-.4 1-.2 1.1.4 2.3.6 3.6.6.6 0 1 .4 1 1V20c0 .6-.4 1-1 1A17 17 0 0 1 3 4c0-.6.4-1 1-1h3.5c.6 0 1 .4 1 1 0 1.3.2 2.5.6 3.6.1.3 0 .7-.2 1z"/></svg></span>
    (580) 472-6193
  </div>
  <div class="contact" style="z-index:2">
    <div class="contact__row"><svg width="14" height="12" viewBox="0 0 24 20"><path fill="#d0141a" d="M5 0h14v5H5zM2 6h20a2 2 0 0 1 2 2v7h-5v5H5v-5H0V8a2 2 0 0 1 2-2zm5 8v4h10v-4z"/></svg>(833) 748-2954</div>
    <div class="contact__row"><svg width="10" height="14" viewBox="0 0 20 28"><path fill="#d0141a" d="M10 0a10 10 0 0 1 10 10c0 7-10 18-10 18S0 17 0 10A10 10 0 0 1 10 0zm0 6a4 4 0 1 0 0 8 4 4 0 0 0 0-8z"/></svg>Cedar Bluff, Harlan, Millbrook</div>
    <div class="contact__row"><svg width="11" height="11" viewBox="0 0 24 24"><circle cx="12" cy="12" r="11" fill="#d0141a"/><path d="M1 12h22M12 1c4 4 4 18 0 22M12 1c-4 4-4 18 0 22" stroke="#161616" stroke-width="1.5" fill="none"/></svg>www.prairieridgepainclinic.com</div>
  </div>
</section>

<section class="card card--back" aria-label="Rack card back">
  <svg class="card__bg" viewBox="0 0 345 770" aria-hidden="true">
    <defs>
      <radialGradient id="backRed" cx="0.45" cy="0.25" r="0.7">
        <stop offset="0" stop-color="#d8171c"/><stop offset="1" stop-color="#8e0c10"/>
      </radialGradient>
    </defs>
    <rect width="345" height="400" fill="url(#backRed)"/>
  </svg>

  <div class="abs lifestyle-photo" role="img" aria-label="Photo of a smiling couple holding hands on a tree-lined autumn path"></div>

  <svg class="card__bg" viewBox="0 0 345 770" aria-hidden="true">
    <path d="M0 310 C120 295 240 300 345 330 L345 350 C240 335 120 340 0 405 Z" fill="#161616"/>
  </svg>

  <div class="abs treat-head">
    <span class="treat-head__line"></span>
    <span class="treat-head__pill">WE TREAT:</span>
    <span class="treat-head__line"></span>
  </div>

  <ul class="treat-list treat-list--left">
    <li style="top:0"><svg width="14" height="14" viewBox="0 0 24 24"><circle cx="12" cy="12" r="10" fill="none" stroke="#ffd0c2" stroke-width="2"/><path d="M7 12l4 4 9-10" fill="none" stroke="#ffd0c2" stroke-width="2.4"/></svg>Car Accident<br>Injuries</li>
    <li style="top:51px"><svg width="14" height="14" viewBox="0 0 24 24"><circle cx="12" cy="12" r="10" fill="none" stroke="#ffd0c2" stroke-width="2"/><path d="M7 12l4 4 9-10" fill="none" stroke="#ffd0c2" stroke-width="2.4"/></svg>Most Personal<br>Injuries</li>
    <li style="top:100px"><svg width="14" height="14" viewBox="0 0 24 24"><circle cx="12" cy="12" r="10" fill="none" stroke="#ffd0c2" stroke-width="2"/><path d="M7 12l4 4 9-10" fill="none" stroke="#ffd0c2" stroke-width="2.4"/></svg>Motorcycle<br>Accident<br>Injuries</li>
    <li style="top:172px"><svg width="14" height="14" viewBox="0 0 24 24"><circle cx="12" cy="12" r="10" fill="none" stroke="#ffd0c2" stroke-width="2"/><path d="M7 12l4 4 9-10" fill="none" stroke="#ffd0c2" stroke-width="2.4"/></svg>Whiplash</li>
    <li style="top:204px"><svg width="14" height="14" viewBox="0 0 24 24"><circle cx="12" cy="12" r="10" fill="none" stroke="#ffd0c2" stroke-width="2"/><path d="M7 12l4 4 9-10" fill="none" stroke="#ffd0c2" stroke-width="2.4"/></svg>Back Injuries</li>
  </ul>
  <div class="abs treat-divider"></div>
  <ul class="treat-list treat-list--right">
    <li style="top:0"><svg width="14" height="14" viewBox="0 0 24 24"><circle cx="12" cy="12" r="10" fill="none" stroke="#ffd0c2" stroke-width="2"/><path d="M7 12l4 4 9-10" fill="none" stroke="#ffd0c2" stroke-width="2.4"/></svg>Semi Truck<br>Injuries</li>
    <li style="top:51px"><svg width="14" height="14" viewBox="0 0 24 24"><circle cx="12" cy="12" r="10" fill="none" stroke="#ffd0c2" stroke-width="2"/><path d="M7 12l4 4 9-10" fill="none" stroke="#ffd0c2" stroke-width="2.4"/></svg>Slip and<br>Falls</li>
    <li style="top:100px"><svg width="14" height="14" viewBox="0 0 24 24"><circle cx="12" cy="12" r="10" fill="none" stroke="#ffd0c2" stroke-width="2"/><path d="M7 12l4 4 9-10" fill="none" stroke="#ffd0c2" stroke-width="2.4"/></svg>Shoulder<br>Injuries</li>
    <li style="top:151px"><svg width="14" height="14" viewBox="0 0 24 24"><circle cx="12" cy="12" r="10" fill="none" stroke="#ffd0c2" stroke-width="2"/><path d="M7 12l4 4 9-10" fill="none" stroke="#ffd0c2" stroke-width="2.4"/></svg>Neck<br>Injuries</li>
    <li style="top:204px"><svg width="14" height="14" viewBox="0 0 24 24"><circle cx="12" cy="12" r="10" fill="none" stroke="#ffd0c2" stroke-width="2"/><path d="M7 12l4 4 9-10" fill="none" stroke="#ffd0c2" stroke-width="2.4"/></svg>Headaches</li>
  </ul>

  <div class="staff staff--one" role="img" aria-label="Portrait of the physician in green scrubs"></div>
  <div class="staff staff--two" role="img" aria-label="Portrait of a staff member in a red top"></div>

  <svg class="card__bg" viewBox="0 0 345 770" aria-hidden="true" style="z-index:1">
    <path d="M0 700 C120 682 240 676 345 700 L345 770 L0 770 Z" fill="#161616"/>
    <path d="M250 672 C290 676 320 684 345 698 L345 706 C318 694 290 686 250 680 Z" fill="#d0141a"/>
  </svg>

  <div class="phone-pill">
    <span class="phone-pill__icon"><svg width="13" height="13" viewBox="0 0 24 24"><path fill="#d0141a" d="M6.6 10.8a15 15 0 0 0 6.6 6.6l2.2-2.2c.3-.3.7-.4 1-.2 1.1.4 2.3.6 3.6.6.6 0 1 .4 1 1V20c0 .6-.4 1-1 1A17 17 0 0 1 3 4c0-.6.4-1 1-1h3.5c.6 0 1 .4 1 1 0 1.3.2 2.5.6 3.6.1.3 0 .7-.2 1z"/></svg></span>
    (580) 472-6193
  </div>
  <div class="contact" style="z-index:2">
    <div class="contact__row"><svg width="14" height="12" viewBox="0 0 24 20"><path fill="#d0141a" d="M5 0h14v5H5zM2 6h20a2 2 0 0 1 2 2v7h-5v5H5v-5H0V8a2 2 0 0 1 2-2zm5 8v4h10v-4z"/></svg>(833) 748-2954</div>
    <div class="contact__row"><svg width="10" height="14" viewBox="0 0 20 28"><path fill="#d0141a" d="M10 0a10 10 0 0 1 10 10c0 7-10 18-10 18S0 17 0 10A10 10 0 0 1 10 0zm0 6a4 4 0 1 0 0 8 4 4 0 0 0 0-8z"/></svg>Cedar Bluff, Harlan, Millbrook</div>
    <div class="contact__row"><svg width="11" height="11" viewBox="0 0 24 24"><circle cx="12" cy="12" r="11" fill="#d0141a"/><path d="M1 12h22M12 1c4 4 4 18 0 22M12 1c-4 4-4 18 0 22" stroke="#161616" stroke-width="1.5" fill="none"/></svg>www.prairieridgepainclinic.com</div>
  </div>
</section>

</body>
</html>
```